Beschriftung Schulbus zum Thema Solarstrom
Zielgruppe
BRIMHOLTEN plant und baut seit mehr als 20 Jahren Photovoltaikanlagen, die sich durch überdurchschnittliche Erträge und höchste Zuverlässigkeit auszeichnen. Darüber hinaus realisieren wir modernste Batteriesysteme und Ladestationen für Elektroautos.
Aufgabenstellung
Es soll ein Schulbus (siehe PDF) gemäß den Vorgaben seitlich (Fenster max. zu 10%) und Hinten komplett (siehe PDF) möglichst auffällig gestaltet werden. Optische Täuschung oder Fotomontage ist erwünscht, so dass der Bus von jedem gesehen wird und zum Thema Photovoltaik in Erinnerung bleibt. Hinweis: Logo nicht verändern und immer mit weißem Hintergrund!

```html
<!DOCTYPE html>
<html lang="de">
<head>
<meta charset="utf-8">
<title>BRIMHOLTEN – Schulbus Beschriftung</title>
<link rel="stylesheet" href="https://fonts.googleapis.com/css2?family=Open+Sans:wght@400;600&family=Oswald:wght@500&family=Allura&display=swap">
<style>
  :root{
    --paper:#fbfbfb;
    --ink:#2b2b2b;
    --frame:#383838;
    --glass:#bac8bc;
    --sky:#2f8fe0;
    --sky-light:#d9e9f6;
    --cloud:#f3f6f9;
    --car:#d4d6d9;
    --car-dark:#9a9da2;
    --brand:#1e8ee0;
    --tyre:#3a3a3a;
    --rim:#c9c9c9;
    --caption:#4a4a4a;
    --accent-red:#c0392b;
  }
  html,body{margin:0;padding:0;overflow:hidden;background:var(--paper);}
  .sheet{width:1200px;height:849px;display:block;}
  .ground{stroke:var(--ink);stroke-width:2;}
  .outline{fill:none;stroke:var(--ink);stroke-width:2.5;}
  .window-frame{fill:var(--frame);}
  .glass{fill:var(--glass);}
  .tyre{fill:var(--tyre);}
  .rim{fill:var(--rim);stroke:#8a8a8a;stroke-width:3;}
  .hub{fill:#e4e4e4;stroke:#888;stroke-width:2;}
  .roof-unit{fill:#fff;stroke:var(--ink);stroke-width:2;}
  .brand-name{font-family:'Oswald',sans-serif;font-weight:500;fill:var(--brand);}
  .brand-sub{font-family:'Open Sans',sans-serif;font-weight:400;fill:var(--ink);}
  .slogan{font-family:'Allura',cursive;fill:var(--ink);}
  .model-mark{font-family:'Open Sans',sans-serif;font-weight:600;fill:#555;letter-spacing:3px;}
  .make-plate{font-family:'Open Sans',sans-serif;font-weight:600;fill:#333;}
  .caption{font-family:'Open Sans',sans-serif;font-weight:400;fill:var(--caption);}
</style>
</head>
<body>
<svg class="sheet" viewBox="0 0 2296 1624" xmlns="http://www.w3.org/2000/svg">
  <defs>
    <linearGradient id="skyFill" x1="0" y1="0" x2="0" y2="1">
      <stop offset="0" stop-color="#2f8fe0"/>
      <stop offset="0.55" stop-color="#7fb8ea"/>
      <stop offset="1" stop-color="#eef4fa"/>
    </linearGradient>
    <linearGradient id="carFill" x1="0" y1="0" x2="0" y2="1">
      <stop offset="0" stop-color="#2b2b2b"/>
      <stop offset="0.3" stop-color="#3a3a3a"/>
      <stop offset="0.32" stop-color="#e2e3e5"/>
      <stop offset="1" stop-color="#c8cacd"/>
    </linearGradient>
    <radialGradient id="childFill">
      <stop offset="0" stop-color="#f1b79e"/>
      <stop offset="0.6" stop-color="#e0536a"/>
      <stop offset="1" stop-color="#e0536a" stop-opacity="0"/>
    </radialGradient>
  </defs>

  <line class="ground" x1="248" y1="440" x2="2110" y2="440"/>
  <line class="ground" x1="248" y1="1017" x2="2110" y2="1017"/>

  <!-- Left side view -->
  <g class="bus-side bus-left">
    <rect class="roof-unit" x="486" y="96" width="114" height="12"/>
    <path class="roof-unit" d="M628 108 q0-22 22-22 h206 q22 0 22 22z"/>
    <rect class="roof-unit" x="1152" y="96" width="112" height="12"/>
    <path d="M258 108 H1540 q12 0 14 40 V395 q0 7-10 7 H258 q-8 0-8-10 V118 q0-10 8-10z" fill="url(#skyFill)" role="img" aria-label="Himmel mit Wolken als Hintergrundfoto"/>
    <rect x="1045" y="210" width="510" height="192" fill="url(#carFill)" role="img" aria-label="Foto eines silbernen Elektroautos"/>
    <ellipse cx="830" cy="300" rx="80" ry="105" fill="url(#childFill)" role="img" aria-label="Foto eines lachenden Schulkindes mit rotem Ranzen"/>
    <rect class="window-frame" x="290" y="145" width="1240" height="16"/>
    <rect class="window-frame" x="290" y="145" width="10" height="130"/>
    <g class="windows">
      <rect class="glass" x="298" y="161" width="152" height="108"/>
      <rect class="window-frame" x="450" y="161" width="18" height="110"/>
      <rect class="glass" x="470" y="161" width="146" height="108"/>
      <rect class="window-frame" x="617" y="161" width="18" height="110"/>
      <rect class="glass" x="637" y="161" width="146" height="108"/>
      <rect class="window-frame" x="784" y="161" width="18" height="110"/>
      <rect class="glass" x="804" y="161" width="146" height="108"/>
      <rect class="window-frame" x="950" y="161" width="18" height="110"/>
      <rect class="glass" x="970" y="161" width="146" height="108"/>
      <rect class="window-frame" x="1116" y="161" width="18" height="110"/>
      <rect class="glass" x="1136" y="161" width="146" height="60"/>
      <rect class="window-frame" x="1282" y="161" width="18" height="60"/>
      <rect class="glass" x="1302" y="161" width="146" height="50"/>
      <rect class="glass" x="1466" y="161" width="56" height="50"/>
    </g>
    <path d="M296 305 q60-30 170-35 H1040 V280 H470 q-100 5-174 40z" fill="var(--frame)"/>
    <path class="outline" d="M258 108 H1540 q12 0 14 40 V395 q0 7-10 7 H258 q-8 0-8-10 V118 q0-10 8-10z"/>
    <path class="outline" d="M230 172 q-18 5-20 58 M222 176 h30" />
    <text class="model-mark" x="465" y="287" font-size="7">TRANSLINE</text>
    <text class="brand-name" x="614" y="370" font-size="36">BRIMHOLTEN</text>
    <text class="brand-sub" x="664" y="392" font-size="13">Elektro &amp; Solar</text>
    <text class="slogan" x="1245" y="305" font-size="26" transform="rotate(4 1245 305)">Politik und Energiekosten?</text>
    <text class="slogan" x="1242" y="330" font-size="26" transform="rotate(4 1242 330)">Egal! Ich nutze selbstgemachten Strom“</text>
    <g class="wheel"><circle class="tyre" cx="543" cy="380" r="58"/><circle class="rim" cx="543" cy="380" r="32"/><circle class="hub" cx="543" cy="380" r="14"/></g>
    <g class="wheel"><circle class="tyre" cx="1198" cy="380" r="58"/><circle class="rim" cx="1198" cy="380" r="32"/><circle class="hub" cx="1198" cy="380" r="14"/></g>
  </g>

  <!-- Right side view -->
  <g class="bus-side bus-right">
    <rect class="roof-unit" x="540" y="674" width="114" height="12"/>
    <path class="roof-unit" d="M926 686 q0-22 22-22 h206 q22 0 22 22z"/>
    <rect class="roof-unit" x="1205" y="674" width="112" height="12"/>
    <path d="M262 686 H1510 q16 0 28 40 q16 50 16 100 V968 q0 10-10 10 H258 q-8 0-8-10 V696 q0-10 12-10z" fill="url(#skyFill)" role="img" aria-label="Himmel mit Wolken als Hintergrundfoto"/>
    <rect x="252" y="790" width="515" height="188" fill="url(#carFill)" role="img" aria-label="Foto eines silbernen Elektroautos"/>
    <ellipse cx="995" cy="880" rx="80" ry="105" fill="url(#childFill)" role="img" aria-label="Foto eines lachenden Schulkindes mit rotem Ranzen"/>
    <rect class="window-frame" x="276" y="722" width="1240" height="16"/>
    <g class="windows">
      <rect class="glass" x="284" y="738" width="42" height="70"/>
      <rect class="window-frame" x="326" y="738" width="16" height="90"/>
      <rect class="glass" x="344" y="738" width="150" height="60"/>
      <rect class="window-frame" x="494" y="738" width="28" height="90"/>
      <rect class="glass" x="522" y="738" width="146" height="90"/>
      <rect class="window-frame" x="668" y="738" width="18" height="110"/>
      <rect class="glass" x="688" y="738" width="74" height="108"/>
      <rect class="window-frame" x="768" y="738" width="152" height="240"/>
      <rect class="glass" x="778" y="754" width="62" height="110"/>
      <rect class="glass" x="850" y="754" width="62" height="110"/>
      <rect class="glass" x="778" y="888" width="62" height="82"/>
      <rect class="glass" x="850" y="888" width="62" height="82"/>
      <rect class="glass" x="930" y="738" width="70" height="108"/>
      <rect class="window-frame" x="1000" y="738" width="18" height="110"/>
      <rect class="glass" x="1020" y="738" width="146" height="108"/>
      <rect class="window-frame" x="1166" y="738" width="22" height="110"/>
      <rect class="glass" x="1190" y="738" width="150" height="108"/>
      <rect class="window-frame" x="1350" y="738" width="50" height="125"/>
      <rect class="glass" x="1360" y="738" width="32" height="108"/>
      <rect class="window-frame" x="1402" y="738" width="112" height="240"/>
      <rect class="glass" x="1410" y="754" width="90" height="110"/>
      <rect class="glass" x="1410" y="888" width="90" height="82"/>
    </g>
    <path class="outline" d="M262 686 H1510 q16 0 28 40 q16 50 16 100 V968 q0 10-10 10 H258 q-8 0-8-10 V696 q0-10 12-10z"/>
    <path class="outline" d="M1520 742 h50 q12 0 16 30 v28 h-8"/>
    <text class="model-mark" x="1230" y="862" font-size="7">TRANSLINE</text>
    <text class="brand-name" x="1043" y="947" font-size="36">BRIMHOLTEN</text>
    <text class="brand-sub" x="1091" y="969" font-size="13">Elektro &amp; Solar</text>
    <text class="slogan" x="310" y="895" font-size="26" transform="rotate(-4 310 895)">Politik und Energiekosten?</text>
    <text class="slogan" x="310" y="920" font-size="26" transform="rotate(-4 310 920)">Egal! Ich nutze selbstgemachten Strom“</text>
    <g class="wheel"><circle class="tyre" cx="605" cy="958" r="58"/><circle class="rim" cx="605" cy="958" r="32"/><circle class="hub" cx="605" cy="958" r="14"/></g>
    <g class="wheel"><circle class="tyre" cx="1260" cy="958" r="58"/><circle class="rim" cx="1260" cy="958" r="32"/><circle class="hub" cx="1260" cy="958" r="14"/></g>
  </g>

  <!-- Front view -->
  <g class="bus-front">
    <path d="M1868 90 H2088 q12 0 18 30 V400 H1845 V120 q4-30 23-30z" fill="#fff" stroke="var(--ink)" stroke-width="2.5"/>
    <path d="M1868 90 H2088 q12 0 18 30 V140 H1848 V120 q4-30 20-30z" fill="var(--sky)"/>
    <rect class="window-frame" x="1845" y="125" width="264" height="185" rx="18"/>
    <rect class="glass" x="1852" y="130" width="250" height="165" rx="14"/>
    <path d="M1885 310 l130-25 M1950 292 l120 20" stroke="var(--ink)" stroke-width="3"/>
    <rect class="window-frame" x="1822" y="176" width="20" height="52" rx="6"/>
    <rect class="window-frame" x="2112" y="176" width="20" height="52" rx="6"/>
    <text class="brand-name" x="1945" y="338" font-size="13">BRIMHOLTEN</text>
    <rect x="1900" y="350" width="156" height="18" fill="#bdbdbd" stroke="#666"/>
    <text class="make-plate" x="1978" y="364" font-size="14" text-anchor="middle">VARNO</text>
    <circle cx="1870" cy="362" r="14" fill="#ddd" stroke="#555" stroke-width="2"/>
    <circle cx="2086" cy="362" r="14" fill="#ddd" stroke="#555" stroke-width="2"/>
    <rect x="1910" y="380" width="136" height="20" fill="#4a4a4a"/>
    <rect class="tyre" x="1848" y="400" width="62" height="40"/>
    <rect class="tyre" x="2044" y="400" width="62" height="40"/>
    <line x1="1978" y1="76" x2="1978" y2="452" stroke="var(--ink)" stroke-width="1"/>
  </g>

  <!-- Rear view -->
  <g class="bus-rear">
    <path d="M1880 670 H2076 q30 0 32 40 V965 H1845 V710 q4-40 35-40z" fill="url(#skyFill)" stroke="var(--ink)" stroke-width="2.5" role="img" aria-label="Himmel mit Wolken als Hintergrundfoto"/>
    <path d="M1868 712 H2086 l-8 70 q-2 16-20 16 H1896 q-18 0-20-16z" fill="var(--frame)"/>
    <path d="M1874 716 H2080 l-6 60 q-2 12-16 12 H1898 q-14 0-16-12z" fill="var(--glass)"/>
    <text class="make-plate" x="1975" y="797" font-size="11" fill="#fff" text-anchor="middle" style="fill:#fff">VARNO</text>
    <ellipse cx="2055" cy="868" rx="36" ry="44" fill="url(#childFill)" role="img" aria-label="Foto eines lachenden Schulkindes"/>
    <text class="brand-name" x="1912" y="892" font-size="24">BRIMHOLTEN</text>
    <text class="brand-sub" x="1950" y="912" font-size="10">Elektro &amp; Solar</text>
    <path d="M1850 860 q12 40 14 80" stroke="var(--accent-red)" stroke-width="6" fill="none"/>
    <path d="M2104 860 q-12 40-14 80" stroke="var(--accent-red)" stroke-width="6" fill="none"/>
    <path d="M1894 918 H2058 l10 48 H1884z" fill="#333"/>
    <rect class="tyre" x="1850" y="965" width="62" height="52"/>
    <rect class="tyre" x="2040" y="965" width="62" height="52"/>
    <line x1="1976" y1="660" x2="1976" y2="994" stroke="var(--ink)" stroke-width="1"/>
  </g>

  <text class="caption" x="2185" y="1528" font-size="48" text-anchor="end">TRANSLINE LE 12M 2P // 13.09.2013</text>
</svg>
</body>
</html>
```